Healthcare technology firm needs business card layout. Logo provided.

We need a business card design for a new healthcare technology company called Mirvela.com. The logo is already done so that will be used in the design. We assist patients and their families manage their personal health finances. Our initial product is our web site membership that includes educational content on your health benefits, tools, and downloadable forms.

We would like to see designs that use our existing logo or extend the logo in a creative way. Should be very consumer friendly.

```html
<!DOCTYPE html>
<html lang="en">
<head>
<meta charset="utf-8">
<title>Mirvela.com business card concepts</title>
<link href="https://fonts.googleapis.com/css2?family=Ubuntu:wght@400;500;700&family=Tinos&display=swap" rel="stylesheet">
<style>
  :root {
    --blue-deep: #0b3f95;
    --blue: #0a6fc9;
    --blue-bright: #1591dc;
    --green: #6cc02e;
    --green-dark: #3a9b2c;
    --black: #000;
    --white: #fff;
    --grey-text: #333;
  }
  * { margin: 0; padding: 0; box-sizing: border-box; }
  html, body { width: 927px; height: 1200px; overflow: hidden; background: var(--white); }
  .sheet {
    position: relative; width: 1020px; height: 1320px;
    transform: scale(0.90882); transform-origin: 0 0;
    font-family: "Ubuntu", sans-serif;
  }
  .stage { position: absolute; left: 2px; top: 0; width: 1018px; height: 765px; background: var(--black); }
  .sheet-title { position: absolute; top: 15px; left: 0; width: 1000px; text-align: center; color: var(--white); font-size: 15px; font-weight: 500; }
  .side-label { position: absolute; color: var(--white); font-family: "Tinos", serif; font-size: 18px; }
  .card { position: absolute; overflow: hidden; }
  .card svg.bg { position: absolute; inset: 0; width: 100%; height: 100%; }
  .abs { position: absolute; }
  .wordmark { font-weight: 500; letter-spacing: -0.5px; line-height: 1; white-space: nowrap; }
  .dot { display: inline-block; border-radius: 50%; vertical-align: middle; margin-right: 8px; }
  .name { font-weight: 500; font-size: 19px; }
  .role { font-size: 12px; }
  .lines { font-size: 13px; line-height: 20px; }

  /* Card 1 front */
  .front { left: 60px; top: 60px; width: 424px; height: 244px; background: linear-gradient(180deg, var(--blue) 0%, var(--blue-deep) 100%); }
  .front .wordmark { left: 0; width: 424px; top: 95px; text-align: center; color: var(--white); font-size: 52px; }
  .front .dot { width: 14px; height: 14px; background: var(--green); }
  .front .tagline { left: 0; width: 424px; top: 210px; text-align: center; color: var(--green); font-weight: 700; font-size: 15px; }

  /* Card 1 back */
  .back { left: 537px; top: 60px; width: 423px; height: 244px; background: var(--white); }
  .back .name { left: 26px; top: 40px; color: var(--green-dark); font-size: 21px; font-weight: 400; }
  .back .role { left: 26px; top: 66px; color: var(--grey-text); }
  .back .lines { left: 26px; top: 103px; color: var(--grey-text); }
  .back .wordmark { right: 22px; top: 97px; color: var(--blue-deep); font-size: 34px; }
  .back .dot { width: 10px; height: 10px; background: var(--green); }
  .back .band-blue { left: 0; bottom: 0; width: 226px; height: 33px; background: linear-gradient(180deg, var(--blue-bright), var(--blue-deep)); }
  .back .band-green { left: 226px; bottom: 0; width: 197px; height: 33px; background: var(--green); }

  /* Card 2 wave */
  .wave { left: 60px; top: 425px; width: 424px; height: 244px; background: var(--white); }
  .wave .wordmark { left: 20px; top: 30px; color: var(--blue-deep); font-size: 44px; }
  .wave .dot { width: 11px; height: 11px; background: var(--green); }
  .wave .name { left: 67px; top: 152px; color: var(--white); }
  .wave .role { left: 67px; top: 175px; color: var(--white); }
  .wave .lines { color: var(--white); }
  .wave .place { left: 67px; top: 194px; }
  .wave .contact { left: 243px; top: 193px; }

  /* Card 3 vertical */
  .vertical { left: 624px; top: 427px; width: 244px; height: 424px; background: var(--white); }
  .vertical .wordmark { left: 0; width: 244px; top: 52px; text-align: center; color: var(--blue-deep); font-size: 36px; }
  .vertical .dot { width: 10px; height: 10px; background: var(--green); }
  .vertical .info { left: 0; width: 244px; text-align: center; color: var(--white); }
  .vertical .name { top: 180px; }
  .vertical .role { top: 204px; }
  .vertical .place { top: 251px; }
  .vertical .contact { top: 300px; }
  .vertical .tagline { left: 0; bottom: 6px; width: 244px; height: 24px; line-height: 24px; background: var(--green); color: var(--white); text-align: center; font-weight: 700; font-size: 14px; }

  /* Card 4 dark top */
  .darktop { left: 60px; top: 853px; width: 424px; height: 244px; background: var(--white); box-shadow: 8px 8px 10px rgba(0,0,0,0.3); overflow: visible; }
  .darktop .wordmark { left: 140px; top: 32px; color: var(--blue-bright); font-size: 44px; }
  .darktop .dot { width: 11px; height: 11px; background: var(--green); }
  .darktop .name { left: 32px; top: 144px; font-size: 15px; font-weight: 700; color: var(--black); }
  .darktop .name small { font-size: 11px; font-weight: 400; }
  .darktop .lines { color: var(--black); }
  .darktop .contact { left: 32px; top: 166px; }
  .darktop .place { left: 233px; top: 163px; }
  .darktop .tagline { left: 0; bottom: 0; width: 424px; height: 27px; line-height: 27px; background: var(--green); color: var(--white); text-align: center; font-weight: 700; font-size: 16px; }

  /* Card 5 dark */
  .dark { left: 537px; top: 996px; width: 423px; height: 244px; background: var(--black); }
  .dark .wordmark { left: 26px; top: 30px; color: var(--blue-bright); font-size: 44px; }
  .dark .dot { width: 11px; height: 11px; background: var(--green); }
  .dark .tagline { left: 26px; top: 103px; color: var(--white); font-weight: 700; font-size: 15px; }
  .dark .rule { left: 262px; top: 114px; width: 133px; height: 1px; background: #888; }
  .dark .place { right: 44px; top: 127px; text-align: right; color: var(--white); }
  .dark .contact { right: 44px; top: 191px; text-align: right; color: var(--white); }
  .dark .name { left: 30px; top: 181px; color: var(--green-dark); font-weight: 700; font-size: 18px; }
  .dark .role { left: 30px; top: 204px; color: var(--white); }
  .dark .strip { right: 0; top: 0; width: 22px; height: 244px; background: linear-gradient(180deg, var(--green) 0%, var(--green) 46%, var(--blue-bright) 47%, var(--blue-deep) 100%); }
</style>
</head>
<body>
<div class="sheet">
  <div class="stage"></div>
  <p class="sheet-title">Improving your health financially</p>

  <section class="card front">
    <div class="abs wordmark"><span class="dot"></span>Mirvela.com</div>
    <p class="abs tagline">Improving your health financially</p>
  </section>
  <p class="side-label" style="left:186px;top:323px;">Front</p>

  <section class="card back">
    <p class="abs name">Dana K. Morrow</p>
    <p class="abs role">CEO</p>
    <p class="abs lines">Elm Harbor, Cedar Point<br>Marlow Bay<br>M:555-014-2276<br>E : dkmorrow@mailbox.net<br>W : mirvela.com</p>
    <div class="abs wordmark"><span class="dot"></span>Mirvela.com</div>
    <div class="abs band-blue"></div>
    <div class="abs band-green"></div>
  </section>
  <p class="side-label" style="left:694px;top:328px;">Back</p>

  <section class="card wave">
    <svg class="bg" viewBox="0 0 424 244" aria-hidden="true">
      <defs>
        <linearGradient id="waveBlue" x1="0" y1="0" x2="0" y2="1">
          <stop offset="0" stop-color="#1591dc"/><stop offset="1" stop-color="#0b3f95"/>
        </linearGradient>
        <path id="taglineCurve" d="M142,108 C220,118 300,140 400,108"/>
      </defs>
      <path d="M0,178 C60,130 160,122 250,130 C330,138 385,132 424,112 L424,244 L0,244Z" fill="url(#waveBlue)"/>
      <path d="M95,128 C190,116 300,145 424,102 L424,116 C330,152 210,132 95,128Z" fill="#6cc02e"/>
      <text font-family="Ubuntu, sans-serif" font-size="12.5" font-weight="700" fill="#0a6fc9"><textPath href="#taglineCurve">IMPROVING YOUR HEALTH FINANCIALLY</textPath></text>
    </svg>
    <div class="abs wordmark"><span class="dot"></span>Mirvela.com</div>
    <p class="abs name">Dana K. Morrow</p>
    <p class="abs role">CEO</p>
    <p class="abs lines place">Elm Harbor, Cedar Point<br>Marlow Bay</p>
    <p class="abs lines contact">M:555-014-2276<br>E : dkmorrow@mailbox.net</p>
  </section>

  <section class="card vertical">
    <svg class="bg" viewBox="0 0 244 424" aria-hidden="true">
      <defs>
        <linearGradient id="vertBlue" x1="0" y1="0" x2="0" y2="1">
          <stop offset="0" stop-color="#1591dc"/><stop offset="1" stop-color="#0b3f95"/>
        </linearGradient>
      </defs>
      <path d="M0,112 L112,160 Q122,165 132,160 L244,112 L244,424 L0,424Z" fill="url(#vertBlue)"/>
    </svg>
    <div class="abs wordmark"><span class="dot"></span>Mirvela.com</div>
    <p class="abs info name">Dana K. Morrow</p>
    <p class="abs info role">CEO</p>
    <p class="abs info lines place">Elm Harbor, Cedar Point<br>Marlow Bay</p>
    <p class="abs info lines contact">M:555-014-2276<br>E : dkmorrow@mailbox.net<br>W : mirvela.com</p>
    <p class="abs tagline">Improving your health financially</p>
  </section>

  <section class="card darktop">
    <svg class="bg" viewBox="0 0 424 244" aria-hidden="true">
      <path d="M0,0 H424 V82 C330,130 240,122 160,106 C90,93 30,100 0,135Z" fill="#000"/>
      <path d="M0,135 C30,100 90,93 160,106 C240,122 330,130 424,82 V88 C330,138 240,130 160,116 C90,104 30,112 0,148Z" fill="#1591dc"/>
    </svg>
    <div class="abs wordmark"><span class="dot"></span>Mirvela.com</div>
    <p class="abs name">Dana K. Morrow, <small>CEO</small></p>
    <p class="abs lines contact">M:555-014-2276<br>E : dkmorrow@mailbox.net</p>
    <p class="abs lines place">Elm Harbor, Cedar Point<br>Marlow Bay</p>
    <p class="abs tagline">Improving your health financially</p>
  </section>

  <section class="card dark">
    <div class="abs wordmark"><span class="dot"></span>Mirvela.com</div>
    <p class="abs tagline">Improving your health financially</p>
    <div class="abs rule"></div>
    <p class="abs lines place">Elm Harbor,<br>Cedar Point<br>Marlow Bay</p>
    <p class="abs lines contact">M:555-014-2276<br>E : dkmorrow@mailbox.net</p>
    <p class="abs name">Dana K. Morrow</p>
    <p class="abs role">CEO</p>
    <div class="abs strip"></div>
  </section>
</div>
</body>
</html>
```